Onsite Energy for Retail Tenants

Need a short one page-3 part build showing how the program for discounted clean energy works - moving into a call to action with multiple links.

1) Solar Garden Produces Energy
2) Credits Available for Tenants’ Utility Bills
3) Sign Up to Receive Utility Bill Credits.
Save 5%

This document will be used:
1) Embedded in Mailchimp emails
2) as an html landing page
3) as an image

Use the latest powerpoint Tenant slide E as guidance
Updates

Infographic is simplistic. 3 part build using graphics and information. Flow is really important so Gifs welcome.

Target Market(s)

Owners of small stores throughout the US.

Industry/Entity Type

Real Estate

Colors

Designer to choose colors to be used in the design.

Requirements
Must have
• It must explain the program clearly and succinctly using the language from the first slide of Mockup 1. This slide must become an elegant build for the 3 step process. See Mockup 2 for its cleanliness ideas for a similar but different program.
• The second slide of mockup 1 is the call to action and must have clickable links and promote trust.
• Please use the attached font styles.
• The text is sparse and so needs to be bold and in order and with the graphics needs to explain how it works perfectly.
• The graphics should be clean and sophisticated but the message and flow needs to be simple.
Nice to have
• Moving arrows to show flow of energy and credits.
• Ability to switch out language of text.

```html
<!DOCTYPE html>
<html lang="en">
<head>
<meta charset="utf-8">
<title>How Clean Discount Electricity Works</title>
<link href="https://fonts.googleapis.com/css2?family=Catamaran:wght@700;800&family=Hind:wght@300;400;500;600&display=swap" rel="stylesheet">
<style>
:root{
  --plum:#58475d;
  --plum-fade:#ffffff;
  --orange:#d77b22;
  --ink:#3a3a3a;
  --line:#cfcfcf;
  --bg:#e9ebec;
  --card:#ffffff;
  --art-solar-top:#fdf3c8;
  --art-solar-bottom:#dfeaf5;
  --art-house-top:#eef3f8;
  --art-house-bottom:#f4e2c8;
  --art-money-top:#fcf3cf;
  --art-money-bottom:#e1efdc;
}
*{box-sizing:border-box;margin:0;padding:0}
html,body{width:1200px;height:923px;overflow:hidden;background:var(--bg)}
.stage{position:absolute;left:0;top:0;width:1300px;height:1000px;transform:scale(.923);transform-origin:0 0;font-family:"Hind",sans-serif;color:var(--ink)}
.card{position:absolute;left:259px;width:782px;height:440px;background:var(--card);box-shadow:0 3px 10px rgba(0,0,0,.18)}
.card--how{top:44px}
.card--offer{top:516px}
.card__title{height:57px;background:linear-gradient(90deg,var(--plum) 0%,var(--plum) 72%,var(--plum-fade) 100%);color:#fff;font-family:"Catamaran",sans-serif;font-weight:800;font-size:38px;line-height:60px;padding-left:18px;letter-spacing:.2px}
.abs{position:absolute}
.num{width:42px;height:42px;border:2px solid var(--ink);border-radius:50%;text-align:center;font-family:"Catamaran",sans-serif;font-weight:800;font-size:27px;line-height:42px}
.step-label{color:var(--orange);font-weight:600;font-size:17px;line-height:20px;text-align:center}
.art{border-radius:4px}
.art--solar{background:linear-gradient(180deg,var(--art-solar-top),var(--art-solar-bottom))}
.art--house{background:linear-gradient(180deg,var(--art-house-top),var(--art-house-bottom))}
.art--money{background:linear-gradient(180deg,var(--art-money-top),var(--art-money-bottom))}
.caption{font-size:15px;line-height:17px;text-align:center}
.caption strong{color:var(--orange);font-weight:600}
.perk{display:flex;gap:2px;font-weight:300;font-size:20px;line-height:20px}
.perk svg{flex:none}
.step{position:absolute;width:272px;height:183px;border:2px solid var(--line);border-top:none;border-radius:14px 14px 0 0;background:#fff}
.step__head{height:42px;margin:0 -2px;background:var(--orange);border-radius:14px 14px 0 0;color:#fff;font-family:"Catamaran",sans-serif;font-weight:800;font-size:23px;display:flex;align-items:center;justify-content:center;gap:10px}
.step__num{width:32px;height:32px;border:2px solid #fff;border-radius:50%;text-align:center;line-height:31px;font-size:21px}
.step__lead{font-weight:500;font-size:15px;line-height:17px;text-align:center;margin-top:18px}
.step__list{list-style:none;margin:26px 0 0 10px;color:var(--orange);font-size:13px;line-height:20px}
.step__list li::before{content:"";display:inline-block;width:7px;height:7px;background:var(--orange);margin-right:6px}
.step__note{color:var(--orange);font-size:13.5px;line-height:20px;margin:18px 0 0 10px}
.btn{position:absolute;width:140px;height:31px;border-radius:9px;background:linear-gradient(90deg,var(--plum) 0 60%,#fff 100%);color:#fff;font-size:15px;line-height:32px;padding-left:30px;text-decoration:none;box-shadow:0 1px 2px rgba(0,0,0,.2)}
.btn svg{position:absolute;right:8px;top:7px}
</style>
</head>
<body>
<div class="stage">

  <section class="card card--how">
    <h1 class="card__title">How Clean Discount Electricity Works?</h1>

    <div class="num abs" style="left:101px;top:69px">1</div>
    <div class="num abs" style="left:368px;top:69px">2</div>
    <div class="num abs" style="left:630px;top:69px">3</div>

    <p class="step-label abs" style="left:62px;top:126px;width:120px">Join a<br>Solar Farm</p>
    <p class="step-label abs" style="left:330px;top:116px;width:116px">Receive<br>Utility Bill<br>Credits</p>
    <p class="step-label abs" style="left:592px;top:134px;width:120px">Save Money</p>

    <svg class="abs" style="left:187px;top:120px" width="140" height="44" viewBox="0 0 140 44" aria-hidden="true">
      <g fill="var(--orange)">
        <polygon points="0,0 12,0 26,22 12,44 0,44 14,22" opacity=".15"/>
        <polygon points="22,0 34,0 48,22 34,44 22,44 36,22" opacity=".3"/>
        <polygon points="44,0 56,0 70,22 56,44 44,44 58,22" opacity=".5"/>
        <polygon points="66,0 78,0 92,22 78,44 66,44 80,22" opacity=".7"/>
        <polygon points="88,0 100,0 114,22 100,44 88,44 102,22" opacity=".85"/>
        <polygon points="110,0 122,0 136,22 122,44 110,44 124,22"/>
      </g>
    </svg>
    <svg class="abs" style="left:450px;top:120px" width="140" height="44" viewBox="0 0 140 44" aria-hidden="true">
      <g fill="var(--orange)">
        <polygon points="0,0 12,0 26,22 12,44 0,44 14,22" opacity=".15"/>
        <polygon points="22,0 34,0 48,22 34,44 22,44 36,22" opacity=".3"/>
        <polygon points="44,0 56,0 70,22 56,44 44,44 58,22" opacity=".5"/>
        <polygon points="66,0 78,0 92,22 78,44 66,44 80,22" opacity=".7"/>
        <polygon points="88,0 100,0 114,22 100,44 88,44 102,22" opacity=".85"/>
        <polygon points="110,0 122,0 136,22 122,44 110,44 124,22"/>
      </g>
    </svg>

    <div class="art art--solar abs" style="left:46px;top:180px;width:160px;height:150px" role="img" aria-label="Illustration of the sun shining on a row of solar panels in a field"></div>
    <div class="art art--house abs" style="left:289px;top:184px;width:204px;height:150px" role="img" aria-label="Illustration of a small house with a blue door among clouds"></div>
    <div class="art art--money abs" style="left:571px;top:171px;width:160px;height:155px" role="img" aria-label="Illustration of a piggy bank in front of fanned banknotes with a sunburst"></div>

    <p class="caption abs" style="left:42px;top:339px;width:160px">Solar Garden<br>Produces Energy &amp;<br>Property receives<br>Utility Credits</p>
    <p class="caption abs" style="left:307px;top:339px;width:160px">Credits Available<br>for Tenants’<br>Utility Bills</p>
    <p class="caption abs" style="left:576px;top:339px;width:160px">Sign Up<br>to Receive Credits<br>on your<br>Utility Bill<br><strong>Save 5%</strong></p>
  </section>

  <section class="card card--offer">
    <h2 class="card__title">Electricity Discount Offer</h2>

    <div class="perk abs" style="left:95px;top:82px">
      <svg width="36" height="36" viewBox="0 0 36 36" aria-hidden="true"><circle cx="16" cy="20" r="14" fill="none" stroke="var(--orange)" stroke-width="3"/><path d="M8 19l7 8L32 3" fill="none" stroke="var(--orange)" stroke-width="4" stroke-linecap="round"/></svg>
      <span>Save 5%<br>on your<br>Electricity Cost</span>
    </div>
    <div class="perk abs" style="left:297px;top:82px">
      <svg width="36" height="36" viewBox="0 0 36 36" aria-hidden="true"><circle cx="16" cy="20" r="14" fill="none" stroke="var(--orange)" stroke-width="3"/><path d="M8 19l7 8L32 3" fill="none" stroke="var(--orange)" stroke-width="4" stroke-linecap="round"/></svg>
      <span>NO Changes<br>to your Utility</span>
    </div>
    <div class="perk abs" style="left:498px;top:82px">
      <svg width="36" height="36" viewBox="0 0 36 36" aria-hidden="true"><circle cx="16" cy="20" r="14" fill="none" stroke="var(--orange)" stroke-width="3"/><path d="M8 19l7 8L32 3" fill="none" stroke="var(--orange)" stroke-width="4" stroke-linecap="round"/></svg>
      <span>NO upfront Cost<br>or Payment</span>
    </div>

    <div class="step" style="left:56px;top:178px">
      <div class="step__head">STEP <span class="step__num">1</span></div>
      <p class="step__lead">Sign Up for the<br>Electricity Discount Agreement.</p>
      <ul class="step__list">
        <li>It runs only for as long as you lease.</li>
        <li>Your Discount is Guaranteed</li>
      </ul>
    </div>

    <svg class="abs" style="left:333px;top:252px" width="96" height="44" viewBox="0 0 96 44" aria-hidden="true">
      <g fill="var(--orange)">
        <polygon points="0,0 12,0 26,22 12,44 0,44 14,22" opacity=".2"/>
        <polygon points="22,0 34,0 48,22 34,44 22,44 36,22" opacity=".45"/>
        <polygon points="44,0 56,0 70,22 56,44 44,44 58,22" opacity=".7"/>
        <polygon points="66,0 78,0 92,22 78,44 66,44 80,22"/>
      </g>
    </svg>

    <div class="step" style="left:429px;top:178px">
      <div class="step__head">STEP <span class="step__num">2</span></div>
      <p class="step__lead" style="margin-top:10px">Securely Provide Brightfield Solar<br>with your Utility information<br>through MeterLink</p>
      <p class="step__note">We use the information only<br>to credit your bill, generate your invoice,<br>and provide clean discounted energy.</p>
    </div>

    <a class="btn" href="#sign-up" style="left:111px;top:377px">Sign Up
      <svg width="10" height="18" viewBox="0 0 10 18" aria-hidden="true"><path d="M1 1l7 8-7 8" fill="none" stroke="var(--orange)" stroke-width="2.5"/></svg></a>
    <a class="btn" href="#contact" style="left:494px;top:377px;padding-left:23px">Contact Us
      <svg width="10" height="18" viewBox="0 0 10 18" aria-hidden="true"><path d="M1 1l7 8-7 8" fill="none" stroke="var(--orange)" stroke-width="2.5"/></svg></a>
  </section>

</div>
</body>
</html>
```